Website for SEO Agency That Serves Family Law Attorneys

I need a design for a website that is clean, conversion focused and professional. The site should have a parallax feel and look very up-to-date. This homepage looks a lot like what I will need https://vemtrosia.com/. I will also need a professional logo that is recognizable and tells users a little about how we do SEO just by looking at it.

```html
<!DOCTYPE html>
<html lang="en">
<head>
<meta charset="utf-8">
<title>Peak Rank SEO – Family Law Attorneys</title>
<link href="https://fonts.googleapis.com/css2?family=Montserrat:wght@300;400;500;700&family=Open+Sans:wght@400;600&display=swap" rel="stylesheet">
<style>
:root{
  --hero-blue:#56679c;
  --hero-deep:#3d4e86;
  --brand-blue:#0166b3;
  --brand-orange:#f26631;
  --teal:#4f968c;
  --teal-deep:#3c7f7a;
  --footer:#3b3b3b;
  --footer-line:#6a6a6a;
  --white:#ffffff;
  --muted:#8a8a8a;
  --navy-text:#1f3c78;
}
*{margin:0;padding:0;box-sizing:border-box}
html,body{width:782px;height:1200px;overflow:hidden;background:var(--white)}
body{position:relative;font-family:'Montserrat',sans-serif;color:var(--white)}
.abs{position:absolute}

/* hero */
.hero{left:0;top:0;width:782px;height:431px;background:linear-gradient(120deg,#4a5b92 0%,var(--hero-blue) 45%,#6373a6 100%)}
.hero-photo{left:0;top:0;width:782px;height:431px;background:radial-gradient(ellipse at 35% 55%,rgba(40,56,110,.55),rgba(40,56,110,0) 60%),radial-gradient(ellipse at 60% 30%,rgba(210,220,240,.25),rgba(210,220,240,0) 55%)}
.header-line{left:0;top:61px;width:782px;height:1px;background:rgba(140,160,230,.6)}
.brand{left:64px;top:22px;display:flex;align-items:center;gap:8px}
.brand-dot{width:18px;height:18px;border-radius:50%;background:var(--white)}
.brand-name{font-size:15px;font-weight:500;letter-spacing:.3px}
.nav{right:64px;top:26px;display:flex;gap:21px;font-size:7.6px;font-weight:500;letter-spacing:.2px}
.hero-title{left:419px;top:161px;font-size:22px;font-weight:300;line-height:30px;white-space:nowrap}
.hero-title strong{display:block;font-weight:700;font-size:22px}
.hero-sub{left:419px;top:224px;width:300px;font-size:10px;line-height:14.5px}
.signup{left:419px;top:261px;width:296px;height:40px;background:var(--white);border-radius:6px}
.signup-field{left:10px;top:14px;font-size:8.8px;color:#444}
.signup-btn{left:215px;top:5px;width:75px;height:31px;background:var(--brand-orange);color:var(--white);font-size:9.5px;display:flex;align-items:center;justify-content:center}

/* info panels */
.panel{top:431px;height:168px}
.panel-do{left:0;width:390px;background:var(--brand-blue)}
.panel-how{left:390px;width:392px;background:var(--brand-orange)}
.panel h2{position:absolute;top:25px;font-size:16px;font-weight:700}
.panel p{position:absolute;top:53px;width:290px;font-size:8px;line-height:14.5px}
.panel-do h2,.panel-do p{left:64px}
.panel-how h2,.panel-how p{left:37px}

/* services */
.services{left:0;top:599px;width:782px;height:303px;background:linear-gradient(100deg,#6a9f94 0%,var(--teal) 45%,var(--teal-deep) 100%)}
.service{top:68px;width:150px;text-align:center}
.service svg{display:block;margin:0 auto}
.service-label{margin-top:11px;font-size:12.3px;font-weight:300}

/* cta */
.cta{left:0;top:902px;width:782px;height:60px;background:var(--brand-orange)}
.cta-text{left:171px;top:20px;font-family:'Open Sans',sans-serif;font-size:13.4px}
.cta-btn{left:475px;top:15px;width:112px;height:32px;background:var(--white);border-radius:16px;color:var(--navy-text);font-family:'Open Sans',sans-serif;font-size:10px;display:flex;align-items:center;justify-content:center}

/* footer */
.footer{left:0;top:962px;width:782px;height:198px;background:var(--footer);font-family:'Open Sans',sans-serif}
.footer h3{position:absolute;top:20px;font-size:11.5px;font-weight:600;letter-spacing:.2px}
.footer h3::after{content:"";position:absolute;left:0;top:21px;width:27px;height:1px;background:var(--white)}
.sitemap{left:64px;top:56px;width:128px;list-style:none;font-size:9px}
.sitemap li{height:23.5px;border-bottom:1px solid var(--footer-line);display:flex;justify-content:space-between;align-items:center;padding:0 1px 2px}
.quote{left:262px;top:57px;width:265px;font-size:9px;line-height:14.5px}
.quote-author{left:262px;top:130px;font-size:9px}
.quote-nav{left:468px;top:138px;display:flex;gap:6px}
.contact-row{left:560px;display:flex;gap:8px;font-size:9px;line-height:14.5px}
.social{left:563px;top:140px;display:flex;gap:9px;font-size:9px;color:var(--muted);font-weight:600}

.legal{left:0;top:1160px;width:782px;height:40px;background:var(--brand-blue);font-family:'Open Sans',sans-serif;font-size:8px;display:flex;align-items:center;justify-content:center}
</style>
</head>
<body>

<section class="abs hero">
  <div class="abs hero-photo" role="img" aria-label="Photo of three business professionals working together at an office desk with a laptop, tinted blue"></div>
  <div class="abs brand"><span class="brand-dot"></span><span class="brand-name">NAME HERE</span></div>
  <nav class="abs nav"><span>ABOUT</span><span>CONTACT</span><span>NEWSLETTER</span></nav>
  <div class="abs header-line"></div>
  <h1 class="abs hero-title">PEAK RANK SEO ( PRS )<strong>FAMILY LAW ATTORNEYS</strong></h1>
  <p class="abs hero-sub">Enter your email below to get access to my proven SEO and traffic tips</p>
  <div class="abs signup">
    <span class="abs signup-field">Email Address</span>
    <span class="abs signup-btn">Sign Up</span>
  </div>
</section>

<section class="abs panel panel-do">
  <h2>WHAT WE DO</h2>
  <p>Lorem Ipsum is simply dummy text of the printing and typesetting industry. Lorem Ipsum has been the industry's standard dummy text ever since the 1500s, when an unknown printer took a galley of type and scrambled it to make a type specimen book.<br>It has survived not only five centuries, but also the leap into electronic typesetting, remaining essentially unchanged.</p>
</section>
<section class="abs panel panel-how">
  <h2>HOW WE DO IT</h2>
  <p>Lorem Ipsum is simply dummy text of the printing and typesetting industry. Lorem Ipsum has been the industry's standard dummy text ever since the 1500s, when an unknown printer took a galley of type and scrambled it to make a type specimen book.<br>It has survived not only five centuries, but also the leap into electronic typesetting, remaining essentially unchanged.</p>
</section>

<section class="abs services" role="img" aria-label="Photo of hands holding paper cut-out family figures, tinted teal">
  <div class="abs service" style="left:57px">
    <svg width="136" height="136" viewBox="0 0 136 136" fill="none" stroke="#fff" stroke-width="1.5">
      <circle cx="68" cy="68" r="67"/>
      <rect x="36" y="41" width="64" height="45" rx="3" stroke-width="5"/>
      <polyline points="48,73 60,62 70,69 84,56" stroke-width="3"/>
      <path d="M52 102h32l-6-8H58z" fill="#fff" stroke="none"/>
    </svg>
    <div class="service-label">Attract More Traffic</div>
  </div>
  <div class="abs service" style="left:230px">
    <svg width="136" height="136" viewBox="0 0 136 136" fill="none" stroke="#fff" stroke-width="1.5">
      <circle cx="68" cy="68" r="67"/>
      <circle cx="68" cy="67" r="29" stroke-width="3.5"/>
      <g fill="#fff" stroke="none">
        <circle cx="68" cy="59" r="6"/><path d="M56 78c0-9 5-12 12-12s12 3 12 12z"/>
        <circle cx="55" cy="63" r="4"/><path d="M46 77c0-6 3-9 9-9 2 0 3 0 4 1-2 2-3 5-3 8z"/>
        <circle cx="81" cy="63" r="4"/><path d="M90 77c0-6-3-9-9-9-2 0-3 0-4 1 2 2 3 5 3 8z"/>
      </g>
    </svg>
    <div class="service-label">Capture More Leads</div>
  </div>
  <div class="abs service" style="left:403px">
    <svg width="136" height="136" viewBox="0 0 136 136" fill="none" stroke="#fff" stroke-width="1.5">
      <circle cx="68" cy="68" r="67"/>
      <g fill="#fff" stroke="none">
        <path d="M68 34l11 6-11 6-11-6z"/><path d="M56 43l11 6v12l-11-6z"/><path d="M80 43l-11 6v12l11-6z"/>
        <path d="M38 52h6v18l14 14v14H45V86L38 76z"/>
        <path d="M98 52h-6v18L78 84v14h13V86l7-10z"/>
      </g>
    </svg>
    <div class="service-label">Nurture Your Prospects</div>
  </div>
  <div class="abs service" style="left:576px">
    <svg width="136" height="136" viewBox="0 0 136 136" fill="none" stroke="#fff" stroke-width="1.5">
      <circle cx="68" cy="68" r="67"/>
      <g stroke="#fff" stroke-width="7" stroke-dasharray="3.5 3.2">
        <circle cx="49" cy="66" r="11"/><circle cx="80" cy="72" r="13"/><circle cx="73" cy="47" r="8"/>
      </g>
      <g stroke="#fff" stroke-width="5">
        <circle cx="49" cy="66" r="8"/><circle cx="80" cy="72" r="10"/><circle cx="73" cy="47" r="5.5"/>
      </g>
    </svg>
    <div class="service-label">Best Solutions</div>
  </div>
</section>

<section class="abs cta">
  <span class="abs cta-text">Start With a Free Law Firm Marketing Analysis</span>
  <span class="abs cta-btn">Get Started</span>
</section>

<footer class="abs footer">
  <h3 style="left:65px">SITE MAP</h3>
  <ul class="abs sitemap">
    <li><span>About</span><span>+</span></li>
    <li><span>Contact</span><span>+</span></li>
    <li><span>Newsletter</span><span>+</span></li>
    <li><span>Privacy Policy</span><span>+</span></li>
    <li><span>Term &amp; Conditions</span><span>+</span></li>
  </ul>

  <h3 style="left:262px">TESTIMONIALS</h3>
  <p class="abs quote">“Lorem Ipsum is simply dummy text of the printing and typesetting industry. Lorem Ipsum has been the industry's standard dummy text to make a type specimen book. versions of Lorem Ipsum.”</p>
  <p class="abs quote-author">”– Dana Morrell</p>
  <div class="abs quote-nav">
    <svg width="20" height="20" viewBox="0 0 20 20" fill="none" stroke="#8a8a8a" stroke-width="1"><circle cx="10" cy="10" r="9.3"/><polyline points="11.5,6 7.5,10 11.5,14"/></svg>
    <svg width="20" height="20" viewBox="0 0 20 20" fill="none" stroke="#8a8a8a" stroke-width="1"><circle cx="10" cy="10" r="9.3"/><polyline points="8.5,6 12.5,10 8.5,14"/></svg>
  </div>

  <h3 style="left:560px">CONTACT US</h3>
  <div class="abs contact-row" style="top:57px">
    <svg width="11" height="14" viewBox="0 0 11 14"><path d="M5.5 0A5.5 5.5 0 0 0 0 5.5C0 9.5 5.5 14 5.5 14S11 9.5 11 5.5A5.5 5.5 0 0 0 5.5 0zm0 7.8a2.3 2.3 0 1 1 0-4.6 2.3 2.3 0 0 1 0 4.6z" fill="#fff"/></svg>
    <span>123 street name, city name,<br>country name</span>
  </div>
  <div class="abs contact-row" style="top:101px">
    <svg width="12" height="12" viewBox="0 0 24 24"><path d="M6.6 10.8a15.1 15.1 0 0 0 6.6 6.6l2.2-2.2c.3-.3.7-.4 1-.2 1.1.4 2.3.6 3.6.6.6 0 1 .4 1 1V20c0 .6-.4 1-1 1A17 17 0 0 1 3 4c0-.6.4-1 1-1h3.5c.6 0 1 .4 1 1 0 1.2.2 2.4.6 3.6.1.3 0 .7-.2 1z" fill="#fff"/></svg>
    <span>02 5550 1420</span>
  </div>
  <div class="abs social"><span>Circlo</span><span>Chirpa</span><span>Plusr</span><span>Linkwise</span></div>
</footer>

<div class="abs legal">All Rights Reserved by domain © 2019</div>

</body>
</html>
```